Clock and Watch Repair

Free quotes. A member of the Guild of Horology Craftsmen of Coral Coast Inc.

At the rear of the card should have the heading QUOTE, DATE and several lines to write in the quote for the customer.

Every time I click on double sided it reverts to single when saved.

THE GEAR WHEEL MEDIC, Leto Marvan [ABN 62 318 904 727], Ph/Fax 9382 7163, Mob 0418 639 254,Email marvanhome@quillnet.example,

```html
<!DOCTYPE html>
<html lang="en">
<head>
<meta charset="utf-8">
<title>The Gear Wheel Medic – Business Card</title>
<link href="https://fonts.googleapis.com/css2?family=Fira+Sans:wght@600;700;800&family=Fjalla+One&display=swap" rel="stylesheet">
<style>
  :root {
    --backdrop: #2a2b2e;
    --sky: #dce7f8;
    --mid-blue: #5a79ad;
    --navy: #0c1d3b;
    --logo-gold: #f7aa1e;
    --accent-orange: #f36a1a;
    --white: #ffffff;
    --ink-navy: #17357a;
    --border-blue: #95b8e8;
    --photo-steel-light: #c9ccd2;
    --photo-steel-dark: #5d6470;
    --photo-gold: #c8a146;
    --photo-skin: #d9a79a;
  }
  * { margin: 0; padding: 0; box-sizing: border-box; }
  html, body {
    width: 1200px; height: 1000px; overflow: hidden;
    background: var(--backdrop);
    font-family: "Fira Sans", Arial, sans-serif;
  }
  .card {
    position: absolute;
    width: 700px; height: 400px;
    overflow: hidden;
    box-shadow: 0 14px 30px rgba(0,0,0,0.45);
  }

  /* Front */
  .card-front {
    left: 110px; top: 70px;
    background: linear-gradient(180deg, var(--sky) 0%, #bcd0ee 30%, var(--mid-blue) 58%, #1d3463 78%, var(--navy) 100%);
  }
  .brand {
    position: absolute; left: 48px; top: 34px;
    display: flex; align-items: center; gap: 14px;
  }
  .brand-dot {
    width: 70px; height: 70px; border-radius: 50%;
    background: var(--logo-gold);
    flex: none;
  }
  .brand-text { display: flex; flex-direction: column; }
  .brand-the {
    font-weight: 800; font-size: 22px; line-height: 1;
    color: var(--logo-gold);
  }
  .brand-name {
    font-weight: 800; font-size: 36px; line-height: 1.1;
    color: var(--logo-gold); white-space: nowrap;
  }
  .tagline {
    font-weight: 700; font-size: 20px; line-height: 1.2; color: var(--white);
    margin-top: 2px;
  }
  .photo-movement {
    position: absolute; left: 368px; top: 200px;
    width: 145px; height: 190px; border-radius: 50%;
    background: radial-gradient(circle at 45% 40%, var(--photo-steel-light), var(--photo-steel-dark));
  }
  .photo-repair {
    position: absolute; left: 520px; top: 22px;
    width: 168px; height: 170px; border-radius: 36px;
    background: linear-gradient(135deg, var(--photo-gold) 0%, var(--photo-steel-light) 55%, var(--photo-skin) 100%);
  }
  .person-name {
    position: absolute; left: 58px; top: 222px;
    font-weight: 700; font-size: 36px; color: var(--accent-orange);
  }
  .contact {
    position: absolute; left: 60px; top: 282px;
    font-weight: 600; font-size: 20px; line-height: 30px; color: var(--white);
    white-space: nowrap;
  }
  .abn {
    position: absolute; right: 18px; top: 352px;
    font-weight: 700; font-size: 16px; color: var(--accent-orange);
    white-space: nowrap;
  }

  /* Back */
  .card-back {
    left: 400px; top: 520px;
    background: var(--border-blue);
  }
  .quote-panel {
    position: absolute; left: 36px; top: 24px; right: 28px; bottom: 28px;
    background: var(--white);
    border-radius: 60px;
  }
  .back-brand {
    position: absolute; left: 0; right: 0; top: 26px;
    text-align: center;
    font-weight: 800; font-size: 26px; color: var(--ink-navy);
    letter-spacing: 1px;
  }
  .field-row {
    position: absolute; left: 62px; right: 58px; top: 98px;
    display: flex; align-items: flex-end; gap: 6px;
  }
  .field-label {
    font-family: "Fjalla One", "Arial Narrow", sans-serif;
    font-size: 28px; line-height: 1; color: var(--ink-navy);
  }
  .field-line {
    border-bottom: 2px solid var(--ink-navy); height: 2px; margin-bottom: 2px;
  }
  .field-line.quote-line { flex: 1.9; }
  .field-line.date-line { flex: 1; }
  .date-label { margin-left: 6px; }
  .write-line {
    position: absolute; left: 62px; right: 58px;
    border-bottom: 2px solid var(--ink-navy);
  }
</style>
</head>
<body>
  <section class="card card-front" aria-label="Business card front">
    <div class="photo-repair" role="img" aria-label="Photo of a hand repairing a gold watch movement with tweezers"></div>
    <div class="photo-movement" role="img" aria-label="Photo of an open steel watch showing its movement"></div>
    <div class="brand">
      <span class="brand-dot" aria-hidden="true"></span>
      <div class="brand-text">
        <span class="brand-the">THE</span>
        <span class="brand-name">GEAR WHEEL MEDIC</span>
        <span class="tagline">Clock And Watch Repair</span>
      </div>
    </div>
    <div class="person-name">Leto Marvan</div>
    <div class="contact">
      Ph/Fax 9382 7163<br>
      Mob. 0418 639 254<br>
      marvanhome@quillnet.example
    </div>
    <div class="abn">ABN 62 318 904 727</div>
  </section>

  <section class="card card-back" aria-label="Business card back">
    <div class="quote-panel">
      <div class="back-brand">THE GEAR WHEEL MEDIC</div>
      <div class="field-row">
        <span class="field-label">QUOTE</span>
        <span class="field-line quote-line"></span>
        <span class="field-label date-label">DATE</span>
        <span class="field-line date-line"></span>
      </div>
      <div class="write-line" style="top:170px"></div>
      <div class="write-line" style="top:225px"></div>
      <div class="write-line" style="top:280px"></div>
    </div>
  </section>
</body>
</html>
```